business card for LWR pty ltd

We require a business card that stands out . I have included our company flyer and would like the services listed to be put on the card so when we Give out the cards to customers they have an idea of services we provide. need the winning design to be in editable photo shop format, editable iMac pages format or editable windows publisher format, so that I can enter in names, email addresses, phone numbers etc myself. I have included a pdf documents of info / items needed on the card to use as reference please.
Updates

need more submissions

Need extra days to review

Sick

Target Market(s)

new customers

Contact Information for Business Card

details are on attached business card requirements file

Requirements
Must have
• I have attached a list of must haves

```html
<!DOCTYPE html>
<html lang="en">
<head>
<meta charset="utf-8">
<title>LWR pty ltd – Business Card</title>
<link href="https://fonts.googleapis.com/css2?family=Krona+One&family=Montserrat:wght@500&family=Open+Sans:wght@400;700&display=swap" rel="stylesheet">
<style>
  :root {
    --backdrop: #4f504f;
    --card-black: #111111;
    --gold: #a57535;
    --band-dark: #3a3a3a;
    --slate: #727272;
    --white: #ffffff;
    --photo-dark: #2a2a2c;
    --photo-warm: #7b6a55;
  }
  * { margin: 0; padding: 0; box-sizing: border-box; }
  html, body { width: 1200px; height: 1200px; overflow: hidden; }
  body { background: var(--backdrop); position: relative; }

  .card {
    position: absolute;
    left: 301px;
    width: 598px;
    height: 342px;
    background: var(--card-black);
    overflow: hidden;
    box-shadow: 4px 5px 8px rgba(0,0,0,0.45);
  }
  .card--services { top: 235px; }
  .card--contact { top: 624px; }
  .card-shapes { position: absolute; inset: 0; width: 598px; height: 342px; }

  .photo {
    position: absolute;
    border-radius: 6px;
  }
  .card--services .photo {
    left: 314px; top: 122px; width: 284px; height: 198px;
    background: linear-gradient(160deg, var(--photo-dark) 0%, #3d3a38 55%, var(--photo-warm) 100%);
  }
  .card--contact .photo {
    left: 256px; top: 19px; width: 342px; height: 161px;
    background: linear-gradient(170deg, #3a3633 0%, var(--photo-dark) 45%, var(--photo-warm) 100%);
  }

  .services-heading {
    position: absolute;
    left: 0; top: 32px;
    width: 199px; height: 34px;
    background: var(--band-dark);
    color: var(--white);
    font-family: "Krona One", sans-serif;
    font-size: 14px;
    line-height: 34px;
    padding-left: 26px;
    letter-spacing: 0.5px;
  }
  .services-list {
    position: absolute;
    left: 26px; top: 86px;
    list-style: none;
    font-family: "Montserrat", sans-serif;
    font-weight: 500;
    font-variant: small-caps;
    font-size: 13px;
    line-height: 17.2px;
    letter-spacing: 1.6px;
    color: var(--white);
  }
  .services-list li { position: relative; padding-left: 11px; }
  .services-list li::before {
    content: "";
    position: absolute; left: 0; top: 7px;
    width: 4px; height: 4px; border-radius: 50%;
    background: var(--white);
  }

  .brand-name {
    position: absolute;
    font-family: "Krona One", sans-serif;
    color: var(--white);
    letter-spacing: 2px;
    line-height: 1;
  }
  .card--services .brand-name { left: 415px; top: 30px; font-size: 42px; }
  .card--contact .brand-name { left: 43px; top: 32px; font-size: 44px; }

  .company-name {
    position: absolute;
    left: 43px; top: 91px;
    font-family: "Krona One", sans-serif;
    font-size: 16px;
    color: var(--white);
    letter-spacing: 1.5px;
  }

  .person {
    position: absolute;
    left: 42px; top: 174px;
    font-family: "Open Sans", sans-serif;
    color: var(--white);
    letter-spacing: 1.5px;
  }
  .person-name { font-size: 16px; font-weight: 700; line-height: 19px; }
  .person-role { font-size: 14px; font-weight: 400; line-height: 20px; }

  .contact-list {
    position: absolute;
    left: 40px; top: 233px;
    list-style: none;
    font-family: "Open Sans", sans-serif;
    font-size: 15px;
    line-height: 20.2px;
    letter-spacing: 1.6px;
    color: var(--white);
  }
  .contact-list li { display: flex; align-items: center; gap: 8px; }
  .contact-icon { width: 12px; height: 12px; flex: none; fill: var(--gold); }
</style>
</head>
<body>

<section class="card card--services">
  <svg class="card-shapes" viewBox="0 0 598 342" aria-hidden="true">
    <polygon points="0,0 438,0 275,342 0,342" fill="var(--gold)"/>
  </svg>
  <div class="photo" role="img" aria-label="Photo of a black road train prime mover with chrome bull bar"></div>
  <div class="services-heading">Our Services:</div>
  <ul class="services-list">
    <li>Over size Loads/Hot Shot Loads</li>
    <li>Heavy Vehicle Recovery Services</li>
    <li>Potable Water Delivers</li>
    <li>Road Building/ Maintenance</li>
    <li>Earthorks</li>
    <li>Sand &amp; Metal Supply &amp; Cartage</li>
    <li>Road Train Tippers</li>
    <li>Road Train Tankers</li>
    <li>Road Train Flat Tops</li>
    <li>Drop Deck Trailers</li>
    <li>Mine Site accredited<br>equipment &amp; Operators</li>
  </ul>
  <div class="brand-name">LWR</div>
</section>

<section class="card card--contact">
  <svg class="card-shapes" viewBox="0 0 598 342" aria-hidden="true">
    <polygon points="317,0 598,0 598,269 267,170" fill="var(--slate)"/>
    <polygon points="0,170 206,170 182,213 0,213" fill="var(--gold)"/>
  </svg>
  <div class="photo" role="img" aria-label="Photo of a road train hauling a yellow grader on a drop deck trailer"></div>
  <div class="brand-name">LWR</div>
  <div class="company-name">LWR PTY LTD</div>
  <div class="person">
    <div class="person-name">Daniel Harlow</div>
    <div class="person-role">Director</div>
  </div>
  <ul class="contact-list">
    <li>
      <svg class="contact-icon" viewBox="0 0 24 24" aria-hidden="true"><path d="M6.6 10.8a15.1 15.1 0 0 0 6.6 6.6l2.2-2.2a1 1 0 0 1 1-.25 11.4 11.4 0 0 0 3.6.57 1 1 0 0 1 1 1V20a1 1 0 0 1-1 1A17 17 0 0 1 3 4a1 1 0 0 1 1-1h3.5a1 1 0 0 1 1 1c0 1.25.2 2.45.57 3.57a1 1 0 0 1-.25 1z"/></svg>
      000 444 000
    </li>
    <li>
      <svg class="contact-icon" viewBox="0 0 24 24" aria-hidden="true"><path d="M2 5h20v14H2z M2 5l10 7 10-7" stroke="var(--card-black)" stroke-width="1.5"/></svg>
      email@lwrservices.com.au
    </li>
    <li>
      <svg class="contact-icon" viewBox="0 0 24 24" aria-hidden="true"><circle cx="12" cy="12" r="10"/><path d="M2 12h20M12 2c3 3 3 17 0 20M12 2c-3 3-3 17 0 20" stroke="var(--card-black)" stroke-width="1.5" fill="none"/></svg>
      www.websiteaddress.com
    </li>
    <li>
      <svg class="contact-icon" viewBox="0 0 24 24" aria-hidden="true"><path d="M12 2a7 7 0 0 0-7 7c0 5 7 13 7 13s7-8 7-13a7 7 0 0 0-7-7zm0 9.5A2.5 2.5 0 1 1 12 6.5a2.5 2.5 0 0 1 0 5z"/></svg>
      Lot 444 example address Australia
    </li>
  </ul>
</section>

</body>
</html>
```